Studio Vela Hair Artists Business Card

I looking for a updated business card for a hair salon and me as a hairstylist. Something stylish and fun but not to whimsical. There has to be some seriousness about it to attract new clients. Basic imformation will be on the card. An abtract head will be okay but not neccessary. If it will fit, I would love to add my "Merrow Crown Wigs" logo and website (www.merrowcrownwigs.example). The "studio Vela Hair Artists logo is not an official logo, but my signage and some other things use that font. I'm open to an variation of the font and format or keep it as is.

Studio Vela
LORETTA QUINN
OWNER / STYLIST

HAIR RELAZING / STRAIGHTENING
EXTENSIONS / WEAVES
CUTS / CUSTOM COLOR
WIGS

20463 Harlow Bend Way, Suite M
Irvine, CA 92614
(949) 555-0182
Email: studiovelahairartists@studiovelahairartists.example
www.studiovelahairartists.example
Updates

Please eliminate "Merrow Crown Wigs" logo...The focus of the b-card is "Studio Vela Hair Artists." The cards I have received so far has merrow crown wigs center stage. If there was room on the card in a side space, the logo would have been okay, but I don't have to have it on the card. Thanks                                   

Industry/Entity Type

Hair

```html
<!DOCTYPE html>
<html lang="en">
<head>
<meta charset="utf-8">
<title>Studio Vela Hair Artists – Business Card</title>
<link rel="stylesheet" href="https://fonts.googleapis.com/css2?family=Open+Sans:wght@300;400&family=Pathway+Gothic+One&family=Architects+Daughter&family=Tinos&display=swap">
<style>
  :root {
    --ink-dark: #242122;
    --ink-deep: #161616;
    --panel-white: #ffffff;
    --slate-top: #6e6e6e;
    --slate-bottom: #3a3a3a;
    --divider: #8c8c8c;
    --accent-aqua: #a9dcdc;
    --accent-pink: #e0198a;
    --text-light: #ffffff;
    --text-mark: #141414;
  }
  * { margin: 0; padding: 0; box-sizing: border-box; }
  html, body { width: 1200px; height: 704px; overflow: hidden; background: var(--ink-deep); }
  .card { position: relative; width: 1200px; height: 704px; overflow: hidden; font-family: "Open Sans", sans-serif; }
  .card-shapes { position: absolute; inset: 0; }
  .card-text { position: absolute; white-space: nowrap; }

  .email { right: 12px; top: 38px; font-family: "Pathway Gothic One", sans-serif; font-size: 33px; color: var(--text-light); font-style: italic; }
  .email .label { color: var(--accent-aqua); }
  .website { left: 566px; width: 634px; text-align: center; top: 128px; font-family: "Tinos", serif; font-size: 39px; color: var(--text-light); }

  .services { left: 700px; width: 460px; top: 244px; list-style: none; text-align: center;
    font-family: "Architects Daughter", cursive; font-size: 29px; line-height: 44px; color: var(--accent-pink); font-style: italic; }

  .brand-mark { left: 30px; width: 470px; top: 312px; text-align: center; color: var(--text-mark); font-weight: 400; }
  .brand-mark .brand-name { display: block; font-size: 66px; line-height: 76px; }
  .brand-mark .brand-sub { display: block; font-size: 22px; letter-spacing: 9px; line-height: 34px; }

  .owner-name { left: 0; width: 625px; top: 546px; text-align: center; font-size: 57px; font-weight: 300; color: var(--text-light); letter-spacing: 1px; }
  .mobile { left: 0; width: 625px; top: 642px; text-align: center; font-size: 33px; font-weight: 300; color: var(--text-light); letter-spacing: 1px; }
  .mobile .label { color: var(--accent-aqua); }

  .address { left: 728px; top: 576px; font-size: 23px; line-height: 37px; color: var(--text-light); }
  .address .label { color: var(--accent-aqua); }
  .address .line-two { display: block; padding-left: 176px; }
</style>
</head>
<body>
<main class="card">
  <svg class="card-shapes" width="1200" height="704" viewBox="0 0 1200 704" aria-hidden="true">
    <defs>
      <linearGradient id="right-field" x1="0" y1="0" x2="1" y2="1">
        <stop offset="0" stop-color="#2a2a2a"/>
        <stop offset="1" stop-color="#111111"/>
      </linearGradient>
      <linearGradient id="slate-field" x1="0" y1="0" x2="0" y2="1">
        <stop offset="0" stop-color="var(--slate-top)"/>
        <stop offset="1" stop-color="var(--slate-bottom)"/>
      </linearGradient>
    </defs>
    <rect class="right-field" width="1200" height="704" fill="url(#right-field)"/>
    <polygon class="left-field" points="0,0 442,0 712,704 0,704" fill="var(--ink-dark)"/>
    <polygon class="slate-field" points="0,480 626,480 712,704 0,704" fill="url(#slate-field)"/>
    <polygon class="mark-band" points="0,270 530,270 613,480 0,480" fill="var(--panel-white)"/>
    <polygon class="divider-line" points="432,0 446,0 716,704 702,704" fill="var(--divider)" opacity="0.55"/>
    <polygon class="services-band" points="602,237 1200,237 1200,502 690,502" fill="var(--panel-white)"/>
  </svg>

  <p class="card-text email"><span class="label">Email:</span> studiovelahairartists@studiovelahairartists.example</p>
  <p class="card-text website">www.studiovelahairartists.example</p>

  <ul class="card-text services">
    <li>HAIR RELAZING</li>
    <li>STRAIGHTENING</li>
    <li>EXTENSIONS</li>
    <li>WEAVES</li>
    <li>CUTS</li>
    <li>CUSTOM COLOR WIGS</li>
  </ul>

  <div class="card-text brand-mark">
    <span class="brand-name">Studio Vela</span>
    <span class="brand-sub">HAIR ARTISTS</span>
  </div>

  <p class="card-text owner-name">LORETTA QUINN</p>
  <p class="card-text mobile"><span class="label">MOBIE:</span> (949) 555-0182</p>

  <p class="card-text address"><span class="label">ADRESS:</span> 20463 Harlow Bend Way, Suite M<span class="line-two">Irvine, CA 92614</span></p>
</main>
</body>
</html>
```